Strength Coach Business Card Design Project

I would like a business card design to complement my new logo. I would like the card to be clean, seek and strong!

Target Market(s)

Mostly adults and junior atheletes who are serious about changing their lives.

Industry/Entity Type

Business

Font styles to use
Serif

Colors

Designer to choose colors to be used in the design.

```html
<!DOCTYPE html>
<html lang="en">
<head>
<meta charset="utf-8">
<title>Ward Strength and Fitness – Business Card</title>
<link rel="stylesheet" href="https://fonts.googleapis.com/css2?family=Exo+2:wght@400;500;700;800&display=swap">
<style>
  :root {
    --backdrop: #3a1212;
    --card: #ffffff;
    --ink: #2b2b2b;
    --muted: #4a4a4a;
    --accent: #e3262b;
    --band: #25272a;
    --ghost: #ececec;
  }
  * { margin: 0; padding: 0; box-sizing: border-box; }
  html, body {
    width: 1200px; height: 800px; overflow: hidden;
    background: var(--backdrop);
    font-family: "Exo 2", sans-serif;
  }
  .card {
    position: absolute; left: 150px; top: 142px;
    width: 900px; height: 515px;
    background: var(--card);
    overflow: hidden;
    box-shadow: 0 18px 40px rgba(0,0,0,.45);
  }
  .brand {
    position: absolute; left: 70px; top: 78px;
    display: flex; align-items: center; gap: 18px;
  }
  .brand-square { width: 74px; height: 74px; background: var(--accent); }
  .brand-name {
    font-weight: 800; font-size: 34px; line-height: 1.02;
    color: var(--ink); text-transform: uppercase; letter-spacing: 1px;
  }
  .ghost-mark {
    position: absolute; right: 70px; top: 60px;
    width: 230px; height: 230px; background: var(--ghost);
  }
  .person { position: absolute; left: 70px; top: 200px; }
  .person-name { color: var(--accent); font-size: 36px; font-weight: 500; line-height: 1.15; }
  .person-role { color: var(--muted); font-size: 21px; margin-top: 2px; letter-spacing: .5px; }
  .contacts { position: absolute; left: 70px; top: 292px; list-style: none; }
  .contacts li {
    display: flex; align-items: center; gap: 12px;
    font-size: 27px; font-weight: 500; color: var(--ink); line-height: 40px;
  }
  .contacts svg { width: 24px; height: 24px; flex: none; }
  .band { position: absolute; left: 0; bottom: 0; width: 900px; height: 150px; }
</style>
</head>
<body>
  <main class="card">
    <div class="ghost-mark" aria-hidden="true"></div>

    <div class="brand">
      <span class="brand-square" aria-hidden="true"></span>
      <span class="brand-name">Ward<br>Strength and Fitness</span>
    </div>

    <div class="person">
      <p class="person-name">Daniel Ward</p>
      <p class="person-role">Strength and Fitness Coach</p>
    </div>

    <ul class="contacts">
      <li>
        <svg viewBox="0 0 24 24" aria-hidden="true"><path fill="#e3262b" d="M6.6 10.8a15.2 15.2 0 0 0 6.6 6.6l2.2-2.2c.3-.3.7-.4 1-.2 1.1.4 2.3.6 3.6.6.6 0 1 .4 1 1V20c0 .6-.4 1-1 1A17 17 0 0 1 3 4c0-.6.4-1 1-1h3.5c.6 0 1 .4 1 1 0 1.3.2 2.5.6 3.6.1.3 0 .7-.2 1z"/></svg>
        0400 123 456
      </li>
      <li>
        <svg viewBox="0 0 24 24" aria-hidden="true"><g fill="none" stroke="#e3262b" stroke-width="2"><circle cx="12" cy="12" r="9.5"/><ellipse cx="12" cy="12" rx="4" ry="9.5"/><path d="M2.5 12h19M4 7h16M4 17h16"/></g></svg>
        www.ward-coaching.co
      </li>
      <li>
        <svg viewBox="0 0 24 24" aria-hidden="true"><rect x="2" y="5" width="20" height="14" fill="#e3262b"/><path d="M2 5l10 8 10-8" fill="none" stroke="#fff" stroke-width="1.8"/></svg>
        Coach@ward-coaching.co
      </li>
    </ul>

    <svg class="band" viewBox="0 0 900 150" preserveAspectRatio="none" aria-hidden="true">
      <polygon points="0,110 900,0 900,150 0,150" fill="var(--accent)"/>
      <polygon points="0,116 900,7 900,150 0,150" fill="var(--band)"/>
    </svg>
  </main>
</body>
</html>
```